Australian tool shop needs a label designed for a new product

we need a label designed for a new product (Velkari Bond) but since its new to the market we want the label to be based on the design of the top 2 existing brands so it is instantly familiar with the customer, attached a photo of the 2 different brands that it needs to look like

Target Market(s)

BRICKLAYERS/ BUILDERS

Industry/Entity Type

Building Product

Requirements
Must have
• MUST HAVE SIMULAR FEELS AS THE UPLOADED IMAGE AND FEEL FAMILIAR WITH THOSE BRANDS

```html
<!DOCTYPE html>
<html lang="en">
<head>
<meta charset="utf-8">
<title>Velkari Bond – Bag Label Variants</title>
<link rel="stylesheet" href="https://fonts.googleapis.com/css2?family=Montserrat:wght@300;600;700;800&display=swap">
<style>
  :root {
    --canvas: #f5f6f8;
    --bag-blue: #354a9f;
    --accent-orange: #e46b1f;
    --ink: #222222;
    --white: #ffffff;
    --icon-tint: #4a5daa;
  }
  html, body {
    margin: 0;
    padding: 0;
    width: 1200px;
    height: 2809px;
    overflow: hidden;
    background: var(--canvas);
  }
  .canvas {
    position: relative;
    width: 1200px;
    height: 2809px;
  }
  .bag-label {
    position: absolute;
    left: 268px;
    width: 660px;
    height: 1045px;
  }
  .bag-label--blue-top { top: 222px; }
  .bag-label--black-top { top: 1539px; }
  .bag-label svg { display: block; }
  .band-blue { fill: var(--bag-blue); }
  .band-orange { fill: var(--accent-orange); }
  .band-black { fill: var(--ink); }
  .product-name-light {
    font-family: 'Montserrat', sans-serif;
    font-weight: 300;
    font-size: 96px;
    fill: var(--ink);
  }
  .product-name-bold {
    font-family: 'Montserrat', sans-serif;
    font-weight: 800;
    font-size: 122px;
    fill: var(--accent-orange);
  }
  .net-weight {
    font-family: 'Montserrat', sans-serif;
    font-weight: 700;
    font-size: 32px;
    fill: var(--bag-blue);
  }
  .product-type {
    font-family: 'Montserrat', sans-serif;
    font-weight: 700;
    font-size: 32px;
    fill: var(--ink);
  }
  .feature-text {
    font-family: 'Montserrat', sans-serif;
    font-weight: 600;
    font-size: 18px;
    fill: var(--white);
  }
  .warning-title {
    font-family: 'Montserrat', sans-serif;
    font-weight: 700;
    font-size: 17px;
    fill: var(--white);
  }
  .warning-body {
    font-family: 'Montserrat', sans-serif;
    font-weight: 600;
    font-size: 7px;
    fill: var(--white);
  }
  .trade-icon-area { fill: var(--icon-tint); }
</style>
</head>
<body>
<main class="canvas">

  <section class="bag-label bag-label--blue-top" aria-label="Velkari Bond bag label, blue top band">
    <svg width="660" height="1045" viewBox="0 0 660 1045">
      <defs>
        <linearGradient id="paperShade" x1="0" y1="0" x2="1" y2="0">
          <stop offset="0" stop-color="#e6e6e6"/>
          <stop offset="0.5" stop-color="#f4f4f4"/>
          <stop offset="1" stop-color="#e4e4e4"/>
        </linearGradient>
      </defs>
      <rect width="660" height="1045" rx="14" fill="url(#paperShade)"/>
      <path class="band-blue" d="M14 0 H646 Q660 0 660 14 V143 Q330 98 0 161 V14 Q0 0 14 0 Z"/>
      <path class="band-black" d="M0 700 C140 760 300 752 420 706 C520 668 600 628 660 598 V1031 Q660 1045 646 1045 H14 Q0 1045 0 1031 Z"/>
      <path class="band-orange" d="M0 708 C150 768 300 762 430 728 C530 702 600 676 660 648 V1031 Q660 1045 646 1045 H14 Q0 1045 0 1031 Z"/>
      <path class="band-blue" d="M0 708 C150 772 300 768 420 742 C520 720 600 706 660 700 V1031 Q660 1045 646 1045 H14 Q0 1045 0 1031 Z"/>

      <text class="product-name-light" x="332" y="312" text-anchor="middle">Velkari</text>
      <text class="product-name-bold" x="332" y="432" text-anchor="middle">BOND</text>
      <text class="net-weight" x="332" y="515" text-anchor="middle">20KG NET</text>
      <text class="product-type" x="332" y="604" text-anchor="middle">PORTLAND CEMENT</text>

      <text class="feature-text" x="54" y="805">Blends with</text>
      <text class="feature-text" x="54" y="826">Sand and Cement easily</text>
      <text class="feature-text" x="56" y="863">Enhannces</text>
      <text class="feature-text" x="56" y="883">Build Quality</text>
      <text class="warning-title" x="58" y="922">WARNING HAZARDOUS</text>
      <text class="warning-body" x="58" y="934">Lorem ipsum dolor sit amet, consectetur adipiscing elit,</text>
      <text class="warning-body" x="58" y="942">sed do eiusmod tempor incididunt ut labore et dolore magna aliqua.</text>
      <text class="warning-body" x="58" y="950">Ut enim ad minim veniam, quis nostrud exercitation ullamco laboris</text>
      <text class="warning-body" x="58" y="958">nisi ut aliquip ex ea commodo consequat.</text>

      <rect class="trade-icon-area" x="414" y="773" width="208" height="185" rx="6" role="img" aria-label="Brick wall and trowel illustration"/>
    </svg>
  </section>

  <section class="bag-label bag-label--black-top" aria-label="Velkari Bond bag label, black top band">
    <svg width="660" height="1045" viewBox="0 0 660 1045">
      <defs>
        <linearGradient id="paperShadeAlt" x1="0" y1="0" x2="1" y2="0">
          <stop offset="0" stop-color="#e6e6e6"/>
          <stop offset="0.5" stop-color="#f2f2f2"/>
          <stop offset="1" stop-color="#e2e2e2"/>
        </linearGradient>
      </defs>
      <rect width="660" height="1045" rx="14" fill="url(#paperShadeAlt)"/>
      <path class="band-black" d="M14 0 H646 Q660 0 660 14 V143 Q330 98 0 161 V14 Q0 0 14 0 Z"/>
      <path class="band-black" d="M0 700 C140 760 300 752 420 706 C520 668 600 628 660 598 V1031 Q660 1045 646 1045 H14 Q0 1045 0 1031 Z"/>
      <path class="band-blue" d="M0 708 C150 772 300 768 420 742 C520 720 600 706 660 700 V1031 Q660 1045 646 1045 H14 Q0 1045 0 1031 Z"/>

      <text class="product-name-light" x="332" y="312" text-anchor="middle">Velkari</text>
      <text class="product-name-bold" x="332" y="432" text-anchor="middle">BOND</text>
      <text class="net-weight" x="332" y="515" text-anchor="middle">20KG NET</text>
      <text class="product-type" x="332" y="604" text-anchor="middle">PORTLAND CEMENT</text>

      <text class="feature-text" x="54" y="805">Blends with</text>
      <text class="feature-text" x="54" y="826">Sand and Cement easily</text>
      <text class="feature-text" x="56" y="863">Enhannces</text>
      <text class="feature-text" x="56" y="883">Build Quality</text>
      <text class="warning-title" x="58" y="922">WARNING HAZARDOUS</text>
      <text class="warning-body" x="58" y="934">Lorem ipsum dolor sit amet, consectetur adipiscing elit,</text>
      <text class="warning-body" x="58" y="942">sed do eiusmod tempor incididunt ut labore et dolore magna aliqua.</text>
      <text class="warning-body" x="58" y="950">Ut enim ad minim veniam, quis nostrud exercitation ullamco laboris</text>
      <text class="warning-body" x="58" y="958">nisi ut aliquip ex ea commodo consequat.</text>

      <rect class="trade-icon-area" x="414" y="773" width="208" height="185" rx="6" role="img" aria-label="Brick wall and trowel illustration"/>
    </svg>
  </section>

</main>
</body>
</html>
```